Quick Banner Ad Job for IT Services Company

Need a collection of banner ads based around a common theme and message.

Main Theme.

IT Support and Managed Services - IT support you can rely on.
Free remote monitoring and alerting*
*conditions apply <-- this in small text

Secondary Content

Our customers are attracted by our exceptional level of customer service and trust us in providing them with support and advice over a long term relationship.

Note:
* Logos and colours attached. Only use these colours.
* Font is to be Myriad Pro

* Delivery will require the following sizes.
Leaderboard: 728×90
Medium Rectangle: 300×250
Wide Skyscraper: 160×600

Do the initial draft in leaderboard, other sizes can be worked once we have an agreed design for the main

Final delivery will also need to be in an editable format, not just final images.

Industry/Entity Type

It Company

```html
<!DOCTYPE html>
<html lang="en">
<head>
<meta charset="utf-8">
<title>TekHaven Leaderboard Banners</title>
<link rel="stylesheet" href="https://fonts.googleapis.com/css2?family=Source+Sans+3:ital,wght@0,400;0,600;0,700;1,400;1,600&display=swap">
<style>
  :root {
    --page: #ffffff;
    --navy-deep: #0b2f4d;
    --navy: #164f7c;
    --sky-deep: #1f95cc;
    --sky: #3bb3e6;
    --ink-navy: #1d3a56;
    --accent-blue: #1c74ba;
    --ink-grey: #333b44;
    --white: #ffffff;
    --frame-grey: #8a8f94;
    --mark-light: #7fd0f2;
    --mark-blue: #1f86c8;
  }
  * { box-sizing: border-box; margin: 0; padding: 0; }
  html, body {
    width: 1200px;
    height: 611px;
    overflow: hidden;
    background: var(--page);
    font-family: "Source Sans 3", "Myriad Pro", sans-serif;
  }
  .banner-set { position: relative; width: 1200px; height: 611px; }
  .banner {
    position: absolute;
    left: 26px;
    width: 1148px;
    height: 145px;
    overflow: hidden;
    box-shadow: 2px 3px 5px rgba(0,0,0,0.35);
  }
  .banner--dark  { top: 40px;  background: linear-gradient(180deg, var(--navy) 0%, var(--navy-deep) 100%); color: var(--white); }
  .banner--white { top: 229px; background: var(--white); border: 1.5px solid var(--frame-grey); color: var(--ink-navy); }
  .banner--light { top: 419px; background: linear-gradient(180deg, var(--sky) 0%, var(--sky-deep) 100%); color: var(--white); }

  .brand { position: absolute; left: 10px; top: 8px; width: 150px; height: 130px; }
  .brand-dot {
    position: absolute; left: 36px; top: 4px;
    width: 72px; height: 72px; border-radius: 50%;
    background: var(--mark-light);
  }
  .banner--white .brand-dot { background: var(--mark-blue); }
  .brand-name {
    position: absolute; left: 2px; top: 72px;
    font-size: 40px; font-weight: 700; line-height: 1;
    letter-spacing: -0.5px;
  }
  .banner--white .brand-name { color: var(--ink-navy); }

  .copy {
    position: absolute; left: 150px; top: 10px; width: 968px;
    text-align: center; white-space: nowrap;
  }
  .headline { font-size: 29px; font-weight: 700; line-height: 36px; letter-spacing: -0.2px; }
  .headline .tagline { font-weight: 400; font-style: italic; letter-spacing: 0; }
  .offer { font-size: 23px; font-weight: 700; line-height: 30px; margin-top: 1px; }
  .banner--white .offer { color: var(--accent-blue); }
  .pitch { font-size: 18px; font-style: italic; line-height: 21px; margin-top: 4px; }
  .banner--white .pitch { color: var(--ink-grey); }

  .conditions {
    position: absolute; right: 12px; bottom: 8px;
    font-size: 13px; font-weight: 600; line-height: 1;
  }
  .banner--white .conditions { color: var(--ink-grey); }
</style>
</head>
<body>
<main class="banner-set">

  <section class="banner banner--dark" aria-label="Leaderboard banner, dark blue">
    <div class="brand"><span class="brand-dot"></span><span class="brand-name">TekHaven</span></div>
    <div class="copy">
      <p class="headline">IT SUPPORT AND MANAGED SERVICES - <span class="tagline">IT support you can rely on.</span></p>
      <p class="offer">Free remote monitoring and alerting*</p>
      <p class="pitch">Our customers are attracted by our exceptional level of customer service and trust us<br>in providing them with support and advice over a long term relationship.</p>
    </div>
    <p class="conditions">*conditions apply</p>
  </section>

  <section class="banner banner--white" aria-label="Leaderboard banner, white">
    <div class="brand"><span class="brand-dot"></span><span class="brand-name">TekHaven</span></div>
    <div class="copy">
      <p class="headline">IT SUPPORT AND MANAGED SERVICES - <span class="tagline">IT support you can rely on.</span></p>
      <p class="offer">Free remote monitoring and alerting*</p>
      <p class="pitch">Our customers are attracted by our exceptional level of customer service and trust us<br>in providing them with support and advice over a long term relationship.</p>
    </div>
    <p class="conditions">*conditions apply</p>
  </section>

  <section class="banner banner--light" aria-label="Leaderboard banner, light blue">
    <div class="brand"><span class="brand-dot"></span><span class="brand-name">TekHaven</span></div>
    <div class="copy">
      <p class="headline">IT SUPPORT AND MANAGED SERVICES - <span class="tagline">IT support you can rely on.</span></p>
      <p class="offer">Free remote monitoring and alerting*</p>
      <p class="pitch">Our customers are attracted by our exceptional level of customer service and trust us<br>in providing them with support and advice over a long term relationship.</p>
    </div>
    <p class="conditions">*conditions apply</p>
  </section>

</main>
</body>
</html>
```